Larkfield Clinic Marketing Flyer

We are a new medical practice in the community and need a flyer to send to other medical offices to inform of our services. We just completed our logo with PixelGuild and would like to incorporate that plus our marketing content into the flyer. Our medical practice has 2 divisions: (1)Mental Health/Psychiatry and (2) Migraine and Neurospasticity Management. Please see website for content and provider photos at www.LarkfieldCare.example

Target Market(s)

Other Healthcare Professionals in the Community

Industry/Entity Type

Medical

Requirements
Must have
• Photos of all 5 healthcare providers, phone number, address, logo

```html
<!DOCTYPE html>
<html lang="en">
<head>
<meta charset="utf-8">
<title>Larkfield Clinic Flyer</title>
<link rel="stylesheet" href="https://fonts.googleapis.com/css2?family=Montserrat:wght@500;600;700&family=Tinos:wght@700&display=swap">
<style>
:root{
  --page:#e4e4e4;
  --sky:#e2e8f4;
  --panel:#f2f5fb;
  --white:#ffffff;
  --green-dark:#1e5e2d;
  --green-head:#1d5a28;
  --green-mid:#6a9a2c;
  --green-lime:#77ad2f;
  --cream:#eef4d8;
  --team-bg:#e9f2df;
  --teal:#1a9a93;
  --ink:#222;
}
*{margin:0;padding:0;box-sizing:border-box}
html,body{width:1200px;height:1200px;overflow:hidden;background:var(--page)}
.flyer{position:absolute;left:188px;top:20px;width:1104px;height:1555px;transform:scale(.746);transform-origin:0 0;background:var(--white);overflow:hidden;font-family:"Montserrat",sans-serif;color:var(--ink);box-shadow:0 6px 24px rgba(0,0,0,.18)}
.sky{position:absolute;left:0;top:0;width:1104px;height:570px;background:var(--sky)}
.left-panel{position:absolute;left:0;top:570px;width:505px;height:602px;background:var(--panel);border-bottom-right-radius:34px}
.stetho{position:absolute;right:0;top:0;width:250px;height:220px;background:radial-gradient(ellipse at 70% 40%,#c9d2de 0%,#dfe5ef 55%,rgba(226,232,244,0) 80%)}
.hero-art{position:absolute;left:0;top:0}
.brand{position:absolute;left:631px;top:38px;width:330px;text-align:center}
.brand-dot{width:96px;height:96px;border-radius:50%;background:var(--teal);margin:0 auto 22px}
.brand-name{font-weight:600;font-size:38px;color:var(--teal);letter-spacing:1px}
.headline{position:absolute;left:636px;top:278px;font-family:"Tinos",serif;font-weight:700;font-size:52px;line-height:61px;color:var(--green-head)}
.services{position:absolute;left:636px;top:476px;font-weight:600;font-size:18.5px;line-height:26px;color:#111}
.divisions-band{position:absolute;left:527px;top:568px;width:577px;height:61px;background:linear-gradient(90deg,var(--green-dark),var(--green-lime));clip-path:polygon(18px 0,100% 0,100% 100%,0 100%);color:#fff;font-weight:700;font-size:21px;padding:17px 0 0 81px}
.block{position:absolute}
.block h2{font-weight:700;font-size:28px;line-height:39px;color:var(--green-head);letter-spacing:-.3px;white-space:nowrap}
.block h2.wrap{white-space:normal}
.block h2.compact{font-size:27px}
.block p{font-weight:500;font-size:18.5px;line-height:25.8px;margin-top:10px;white-space:nowrap}
.block .icon{position:absolute;left:-58px;top:3px;width:42px;height:42px;border-radius:50%;background:radial-gradient(circle at 50% 40%,var(--teal) 0 45%,var(--green-lime) 46%)}
.team{position:absolute;left:0;top:1172px;width:1104px;height:282px;background:var(--team-bg)}
.member{position:absolute;top:20px;width:210px;margin-left:-105px;text-align:center}
.portrait{width:176px;height:176px;border-radius:50%;border:6px solid var(--green-mid);margin:0 auto;background:linear-gradient(160deg,#7f8d96,#4d5a63);box-shadow:0 0 0 3px #fff inset}
.member-name{font-weight:700;font-size:19px;line-height:23px;color:var(--green-head);margin-top:22px}
.footer{position:absolute;left:0;top:1454px;width:1104px;height:101px;background:var(--green-dark);color:#fff}
.phones{position:absolute;left:0;top:0;width:383px;height:101px;background:var(--green-lime);border-top-right-radius:60px 101px}
.phone{position:absolute;left:58px;display:flex;align-items:center;gap:20px;font-weight:700;font-size:24px}
.phone svg,.contact svg{flex:none}
.contact{position:absolute;display:flex;align-items:flex-start;gap:16px;font-weight:500;font-size:18px;line-height:26px}
</style>
</head>
<body>
<div class="flyer">
  <div class="sky"></div>
  <div class="left-panel"></div>
  <div class="stetho" role="img" aria-label="Stethoscope resting on a light surface"></div>

  <svg class="hero-art" width="620" height="800" viewBox="0 0 620 800">
    <defs>
      <linearGradient id="photoTone" x1="0" y1="0" x2="1" y2="1">
        <stop offset="0" stop-color="#f4f4f2"/>
        <stop offset=".5" stop-color="#d9b55a"/>
        <stop offset="1" stop-color="#8a8a86"/>
      </linearGradient>
    </defs>
    <circle cx="236" cy="383" r="404" fill="#fff"/>
    <path d="M 583 240 A 374 374 0 1 0 583 526" fill="none" stroke="var(--green-mid)" stroke-width="54"/>
    <circle cx="236" cy="383" r="318" fill="#fff"/>
    <circle cx="236" cy="383" r="294" fill="none" stroke="var(--cream)" stroke-width="52"/>
    <circle cx="236" cy="383" r="266" fill="url(#photoTone)" role="img" aria-label="Woman in a yellow top smiling at her phone on a sofa"/>
  </svg>

  <div class="brand">
    <div class="brand-dot"></div>
    <div class="brand-name">Larkfield Clinic</div>
  </div>

  <h1 class="headline">Helping Bodies<br>Helping Minds<br>Helping You</h1>
  <p class="services">Mental Health and Psychiatry Services<br>Migraine and Neurospasticity Intervention</p>

  <div class="divisions-band">Our medical practice has 2 divisions:</div>

  <div class="block" style="left:603px;top:655px;width:470px">
    <span class="icon"></span>
    <h2 class="wrap">Migraine &amp; Neurospasticity Management</h2>
    <p>Injections of botulinum neurotoxin are a widely<br>used therapeutic form of treatment for both<br>chronic migraines and patients with involuntary<br>muscle contractions (neurospasticity). Injections<br>may offer up to 3 months of relief and may be<br>combined with other pharmaceutical<br>interventions for maximum benefit</p>
  </div>

  <div class="block" style="left:603px;top:952px;width:470px">
    <span class="icon"></span>
    <h2>Mental Health/Psychiatry</h2>
    <p>Bringing comprehensive evaluation, medication<br>management and psychotherapy to the full<br>spectrum of mental health disorders including<br>minor, moderate and major depression, bipolar<br>disorder, ADD/ADHD, anxiety, schizophrenia,<br>stress or grief reactions, and others</p>
  </div>

  <div class="block" style="left:89px;top:811px;width:400px">
    <span class="icon"></span>
    <h2>New Patient Evaluation</h2>
    <p>Consults provided for evaluation and<br>management of patients with chronic<br>migraines or neurospasticity<br>challenges</p>
  </div>

  <div class="block" style="left:89px;top:990px;width:410px">
    <span class="icon"></span>
    <h2 class="compact">Insurance Pre-Authorization</h2>
    <p>Botulinum toxin injections may be a<br>recommended treatment option.<br>If so, our office completes insurance<br>pre-authorizations on your behalf.</p>
  </div>

  <section class="team">
    <div class="member" style="left:126px"><div class="portrait" role="img" aria-label="Portrait of Martin Ellwood"></div><div class="member-name">Martin Ellwood</div></div>
    <div class="member" style="left:331px"><div class="portrait" role="img" aria-label="Portrait of Helen Marsh"></div><div class="member-name">Helen Marsh,<br>PMHNP</div></div>
    <div class="member" style="left:543px"><div class="portrait" role="img" aria-label="Portrait of Paul Brenner"></div><div class="member-name">Paul Brenner,<br>PMHNP</div></div>
    <div class="member" style="left:752px"><div class="portrait" role="img" aria-label="Portrait of Dale Corwin"></div><div class="member-name">Dale Corwin<br>PMHNP</div></div>
    <div class="member" style="left:973px"><div class="portrait" role="img" aria-label="Portrait of Nora Castell"></div><div class="member-name">Nora Castell,<br>PMHNP</div></div>
  </section>

  <footer class="footer">
    <div class="phones">
      <div class="phone" style="top:18px"><svg width="24" height="24" viewBox="0 0 24 24" fill="none" stroke="#fff" stroke-width="2"><path d="M5 3h4l2 5-3 2a12 12 0 0 0 6 6l2-3 5 2v4a2 2 0 0 1-2 2A18 18 0 0 1 3 5a2 2 0 0 1 2-2z"/></svg>(208) 555-0142</div>
      <div class="phone" style="top:56px"><svg width="24" height="24" viewBox="0 0 24 24" fill="none" stroke="#fff" stroke-width="2"><path d="M5 3h4l2 5-3 2a12 12 0 0 0 6 6l2-3 5 2v4a2 2 0 0 1-2 2A18 18 0 0 1 3 5a2 2 0 0 1 2-2z"/></svg>(208) 555-0187</div>
    </div>
    <div class="contact" style="left:442px;top:25px"><svg width="28" height="32" viewBox="0 0 24 28" fill="none" stroke="#fff" stroke-width="1.8"><path d="M12 2a8 8 0 0 0-8 8c0 6 8 14 8 14s8-8 8-14a8 8 0 0 0-8-8z"/><circle cx="12" cy="10" r="3"/><path d="M5 26h14"/></svg><span>412 W. Alder Ave.<br>Brookmere, ID - 83800</span></div>
    <div class="contact" style="left:766px;top:25px"><svg width="26" height="26" viewBox="0 0 24 24" fill="none" stroke="#fff" stroke-width="1.6"><circle cx="12" cy="12" r="10"/><ellipse cx="12" cy="12" rx="4.5" ry="10"/><path d="M2 12h20M4 7h16M4 17h16"/></svg><span>www.LarkfieldCare.example</span></div>
  </footer>
</div>
</body>
</html>
```